Creation of a Nutrition Consulting Flyer. For more information please see attached word document.

Industry/Entity Type

Health Service

Requirements
Must have
• Contend please see word document
The 3 fold flyer must meet the requirements of the DL formats, which is 210mm x 99 mm or for non 3 fold flyers DIN A 5 which is 210 mm x 148 mm (folded or non folded).
Nice to have
• our current idea is a 3 fold flyer but i am more than happy to receive other formats that better present the contend provided.

```html
<!DOCTYPE html>
<html lang="en">
<head>
<meta charset="utf-8">
<title>Nutritional Coaching – DL Trifold, Inside</title>
<link href="https://fonts.googleapis.com/css2?family=Amatic+SC:wght@700&family=Open+Sans:wght@400;600;700&display=swap" rel="stylesheet">
<style>
  :root{
    --sage:#6e7772;
    --sage-dark:#5f6863;
    --salmon:#e7968a;
    --salmon-strong:#e98a78;
    --charcoal:#393c3f;
    --ink:#ffffff;
    --page:#f1f1f1;
  }
  *{box-sizing:border-box;margin:0;padding:0}
  html,body{width:1200px;height:800px;overflow:hidden;background:var(--page)}
  body{font-family:"Open Sans",Arial,sans-serif;color:var(--ink)}
  .flyer{position:absolute;left:60px;top:18px;width:1080px;height:764px;overflow:hidden;background:var(--sage);box-shadow:0 4px 18px rgba(0,0,0,.12)}
  .flyer-shapes{position:absolute;inset:0}
  .fold{position:absolute;top:0;width:1px;height:100%;background:rgba(0,0,0,.08)}
  .panel{position:absolute;top:0;width:360px;height:100%}
  .panel--about{left:0}
  .panel--services{left:360px}
  .panel--cover{left:720px}
  .hand-title{font-family:"Amatic SC",cursive;font-weight:700;font-size:28px;line-height:1.1;letter-spacing:1px;text-transform:uppercase}
  .rule{height:1.5px;background:var(--ink);margin:12px 0 14px}
  .body-copy{font-size:11.8px;line-height:1.5}
  .body-copy p+p{margin-top:10px}
  .panel--about .content{position:absolute;left:24px;top:36px;width:320px}
  .panel--services .content{position:absolute;left:24px;top:36px;width:316px}
  .service{display:flex;gap:14px;align-items:center;margin-bottom:18px}
  .service-icon{flex:0 0 52px;width:52px;height:52px}
  .service h3{color:var(--salmon-strong);font-size:14px;font-weight:700;margin-bottom:3px}
  .service p{font-size:11.8px;line-height:1.5}
  .panel--cover .content{position:absolute;left:34px;top:430px;width:300px}
  .tagline{font-size:13px;font-weight:700;line-height:1.4}
  .cover-title{color:var(--salmon-strong);font-size:32px;margin-bottom:10px}
  .panel--cover .rule{margin:10px 0 10px}
</style>
</head>
<body>
<main class="flyer">
  <svg class="flyer-shapes" viewBox="0 0 1080 764" width="1080" height="764">
    <defs>
      <linearGradient id="coach-photo-tone" x1="0" y1="0" x2="1" y2="1">
        <stop offset="0" stop-color="#4a4d50"/><stop offset="1" stop-color="#2f3134"/>
      </linearGradient>
    </defs>
    <path d="M0 640 C120 618 250 612 360 618 L360 764 L0 764 Z" fill="var(--salmon)"/>
    <path d="M770 0 L1080 0 L1080 330 L800 360 C760 420 720 470 650 520 L600 600 L520 764 L460 764 C520 650 600 560 700 470 C760 400 760 300 720 220 C700 150 730 60 770 0 Z" fill="var(--salmon)"/>
    <path d="M360 670 C400 660 440 660 470 680 L470 764 L360 764 Z" fill="var(--salmon)"/>
    <path d="M560 764 C600 700 620 640 690 590 C740 550 780 500 790 440 C800 380 860 340 960 320 C1020 310 1060 300 1080 290 L1080 764 Z" fill="var(--charcoal)"/>
    <rect x="790" y="330" width="290" height="434" fill="url(#coach-photo-tone)" opacity=".45" role="img" aria-label="Faint portrait of the nutrition coach behind the cover text"/>
    <circle cx="180" cy="718" r="122" fill="none" stroke="#fff" stroke-width="1.2"/>
    <circle cx="180" cy="718" r="112" fill="#9a9a94" role="img" aria-label="Photo of the nutrition coach holding fresh parsley in a kitchen"/>
    <circle cx="612" cy="545" r="112" fill="none" stroke="var(--salmon)" stroke-width="1.2"/>
    <circle cx="612" cy="545" r="104" fill="#8fae6a" role="img" aria-label="Photo of a spinach, tomato and avocado salad"/>
    <circle cx="540" cy="660" r="96" fill="none" stroke="#fff" stroke-width="1.2"/>
    <circle cx="540" cy="660" r="88" fill="#8a6a4d" role="img" aria-label="Photo of sliced wholegrain bread"/>
    <circle cx="470" cy="470" r="22" fill="#fff" opacity=".35"/>
    <circle cx="905" cy="130" r="118" fill="none" stroke="#fff" stroke-width="1"/>
    <circle cx="905" cy="130" r="110" fill="#c9b47e" role="img" aria-label="Photo of pasta salad with rocket and peppers"/>
    <circle cx="860" cy="305" r="90" fill="none" stroke="var(--salmon)" stroke-width="1.2"/>
    <circle cx="860" cy="305" r="82" fill="#7e9a5c" role="img" aria-label="Photo of a mixed salad with cucumber, carrot and seeds"/>
    <circle cx="960" cy="235" r="30" fill="#fff" opacity=".3"/>
  </svg>
  <div class="fold" style="left:360px"></div>
  <div class="fold" style="left:720px"></div>

  <section class="panel panel--about">
    <div class="content">
      <h2 class="hand-title">My aim is, to perfectly support you to achieve your aims.</h2>
      <div class="rule"></div>
      <div class="body-copy">
        <p>I offer personal as well as online coaching. We could meet at your place, in a café, at my place or online via multiple channels. As your personal coach I will be available to answer your questions or solve your questions in a responsible and binding manner.</p>
        <p>One of the most effective ways you can take to improve your health is to increase your energy level and to prevent chronical diseases, is to alter to a healthy and nutrition diet.</p>
        <p>Whenever there is a desire to change the current condition, coaching can support you on boost this desire for a change to the better. Using suitable questions and tools, we will define your aims and define measures to achieve your goals. You will understand, on what can be changed in your nutrition in order to make the change sustainable. My holistic nutrition coaching is fully tailored to your needs and circumstances. You are the one determining on what shall be done and in which speed. And with my consultation, I am positive that you will master your challenge.</p>
      </div>
    </div>
  </section>

  <section class="panel panel--services">
    <div class="content">
      <h2 class="hand-title">Have healthy eating be your daily routine</h2>
      <div class="rule"></div>
      <div class="service">
        <svg class="service-icon" viewBox="0 0 54 54"><circle cx="27" cy="27" r="25" fill="none" stroke="var(--salmon)" stroke-width="1.5"/><path d="M14 19 L27 22 L40 19 L40 37 L27 40 L14 37 Z M27 22 L27 40" fill="none" stroke="#fff" stroke-width="1.4"/></svg>
        <div><h3>Nutritional information</h3><p>Interesting facts about a healthy diet and the health effects of food.</p></div>
      </div>
      <div class="service">
        <svg class="service-icon" viewBox="0 0 54 54"><circle cx="27" cy="27" r="25" fill="none" stroke="var(--salmon)" stroke-width="1.5"/><rect x="15" y="16" width="24" height="17" fill="none" stroke="#fff" stroke-width="1.4"/><path d="M27 33 L21 41 M27 33 L33 41 M27 13 L27 16" stroke="#fff" stroke-width="1.4"/></svg>
        <div><h3>Nutritional coaching</h3><p>If you are no longer satisfied with your current state, I will accompany and support you in your change process.</p></div>
      </div>
      <div class="service">
        <svg class="service-icon" viewBox="0 0 54 54"><circle cx="27" cy="27" r="25" fill="none" stroke="var(--salmon)" stroke-width="1.5"/><circle cx="27" cy="27" r="9" fill="none" stroke="#fff" stroke-width="1.4"/><path d="M14 16 L14 38 M11 16 L11 23 Q14 26 17 23 L17 16 M40 16 Q36 22 40 27 L40 38" fill="none" stroke="#fff" stroke-width="1.4"/></svg>
        <div><h3>Recipes</h3><p>Simple, healthy and everyday recipes serve as inspiration and should motivate you to try something new.</p></div>
      </div>
    </div>
  </section>

  <section class="panel panel--cover">
    <div class="content">
      <p class="tagline">Your nutritional innovation<br>for more health, beauty, energy and vitality</p>
      <div class="rule"></div>
      <h1 class="hand-title cover-title">Nutritional coaching</h1>
      <div class="body-copy">
        <p>Would you like to eat healthily in the long term and finally be free from diets? Great, then you've come to the right place with me! I'll show you tips and tricks to create changes that work in the long term, nourish your body and can be easily and enjoyably integrated into your everyday life.</p>
        <p>Arrange a free consultation to find out whether my nutrition coaching is right for you.</p>
      </div>
    </div>
  </section>
</main>
</body>
</html>
```